Real Estate Marketing Postcards need a fresh look, Front & Back

I have a current postcard design (attached) that lacks design quality and too much use of color. I do like the basic color scheme, but I'm open to anything that cleans up the look and incorporates space for the existing text. I'm not opposed to a design with a white background, more white space. The design should be full bleed according to the attached specs. I would like this to be sent over in an Adobe format, something like InDesign.

The company logo will remain the same colors and appearance. The headshot will likely be updated in the coming weeks.

I am attaching a sample of a recent card plus a template from the printer showing the back of the card and location of the address and postage section that must remain blank. I am also including the logo and another logo designed for use with a white (or non blue) background.

(feel free to swap in stock photos of whatever house you want, but the front of the card should incorporate at least one photo of a house.)

Target Market(s)

Home owners.

Industry/Entity Type

Real Estate

Font styles to use
Sans Serif

Colors

Designer to choose colors to be used in the design.

Requirements
Must have
• Company logo, the headshot, the contact info on the back, a photo or photos of a house along with the text "Just Sold" or "Sold" featured on the front of the card.

```html
<!DOCTYPE html>
<html lang="en">
<head>
<meta charset="utf-8">
<title>Willowbrook Real Estate – Just Sold Postcard</title>
<link rel="stylesheet" href="https://fonts.googleapis.com/css2?family=Open+Sans:wght@400;600;700;800&display=swap">
<style>
  :root{
    --navy:#0d4f8b;
    --navy-deep:#0a3f70;
    --lime:#8cc63f;
    --sold-red:#c8232c;
    --paper:#ffffff;
    --stage:#eef1f5;
    --text-blue:#1a5a96;
    --muted:#5a6f86;
    --hairline:#d6dee8;
  }
  *{margin:0;padding:0;box-sizing:border-box}
  html,body{width:1200px;height:1200px;overflow:hidden;background:var(--stage)}
  body{position:relative;font-family:"Open Sans",sans-serif;color:var(--text-blue)}

  .card{position:absolute;width:760px;height:540px;background:var(--paper);
    box-shadow:0 2px 10px rgba(10,40,80,.12);overflow:hidden}

  /* FRONT */
  .card-front{left:60px;top:40px}
  .house-photo{position:absolute;left:24px;top:24px;width:712px;height:392px;
    background:linear-gradient(180deg,#6fa4dc 0%,#a9cbeb 32%,#d6c7a4 52%,#b9a27f 70%,#cdb891 100%)}
  .sold-tag{position:absolute;left:24px;top:380px;height:36px;padding:0 18px;background:var(--sold-red);
    color:#fff;font-weight:700;font-size:14px;letter-spacing:3px;line-height:36px;white-space:nowrap}
  .front-footer{position:absolute;left:24px;right:24px;top:416px;bottom:0;
    display:flex;align-items:center;justify-content:space-between;border-bottom:6px solid var(--navy)}
  .headline{font-size:58px;font-weight:800;color:var(--navy);letter-spacing:-1px;line-height:1;white-space:nowrap}
  .headline .accent{color:var(--sold-red)}
  .brand{display:flex;align-items:center;gap:10px;white-space:nowrap}
  .brand-square{width:14px;height:14px;background:var(--lime)}
  .brand-name{font-weight:700;font-size:22px;color:var(--navy)}

  /* BACK */
  .card-back{left:380px;top:620px}
  .back-header{position:absolute;left:0;top:0;width:100%;height:90px;background:var(--navy);border-bottom:4px solid var(--lime)}
  .back-header .brand{position:absolute;right:30px;top:30px}
  .back-header .brand-name{color:#fff}
  .headshot{position:absolute;left:30px;top:28px;width:130px;height:130px;border:4px solid #fff;
    box-shadow:0 1px 4px rgba(0,0,0,.2);
    background:radial-gradient(circle at 50% 40%,#c6b7ae 0%,#a79a98 45%,#8d8a96 100%)}
  .agent{position:absolute;left:30px;top:172px;width:170px;font-size:12px;line-height:16px;color:var(--muted)}
  .agent-name{font-size:18px;font-weight:700;color:var(--navy);line-height:22px}
  .agent-tag{font-size:14px;line-height:20px;color:var(--text-blue);margin-bottom:4px}
  .badges{position:absolute;left:30px;top:310px;display:flex;gap:6px;align-items:flex-end}
  .badge{background:var(--hairline);border-radius:2px}
  .pitch{position:absolute;left:214px;top:106px;width:516px}
  .pitch h1{font-size:40px;font-weight:800;color:var(--navy);line-height:48px;letter-spacing:-.5px}
  .pitch .lead{font-size:16px;line-height:22px;font-weight:600;color:var(--text-blue)}
  .pitch p{font-size:13px;line-height:18px;margin-top:8px;color:var(--muted)}
  .pitch .cta{color:var(--navy);font-weight:600}
  .pitch .cta .sold{color:var(--sold-red);font-weight:800}
  .fineprint{font-size:7px;line-height:9px;margin-top:6px;color:var(--muted)}
  .address-rule{position:absolute;left:30px;right:30px;top:350px;height:1px;background:var(--hairline)}
</style>
</head>
<body>

<section class="card card-front">
  <div class="house-photo" role="img" aria-label="Photo of a two-storey craftsman house with stone base, beige siding and gabled roof under a blue sky"></div>
  <div class="sold-tag">SOLD</div>
  <div class="front-footer">
    <div class="headline">JUST <span class="accent">SOLD</span></div>
    <div class="brand"><span class="brand-square"></span><span class="brand-name">willowbrook</span></div>
  </div>
</section>

<section class="card card-back">
  <header class="back-header">
    <div class="brand"><span class="brand-square"></span><span class="brand-name">willowbrook</span></div>
  </header>
  <div class="headshot" role="img" aria-label="Agent headshot"></div>
  <div class="agent">
    <div class="agent-name">Dario Castellano</div>
    <div class="agent-tag">“The Fernwood Realtor”</div>
    <div>Principal Broker, REALTOR</div>
    <div>Willowbrook Real Estate</div>
    <div>555.410.2200 Office</div>
    <div>555.628.7143 Cell</div>
    <div>www.FernwoodHomesite.com</div>
  </div>
  <div class="badges">
    <span class="badge" style="width:22px;height:20px"></span>
    <span class="badge" style="width:28px;height:16px"></span>
    <span class="badge" style="width:18px;height:18px"></span>
  </div>
  <div class="pitch">
    <h1>Selling?</h1>
    <div class="lead">Choosing the right agent is critical to your success.</div>
    <p>Your home is your biggest asset.</p>
    <p>You owe it to yourself to have every advantage by choosing the local agent with the expertise to position your Fernwood home and get it sold fast and for top dollar.</p>
    <p>There is no other agent who knows the Fernwood market better.</p>
    <p class="cta">Contact me today to get your home <span class="sold">SOLD!</span></p>
    <div class="fineprint">If your home is currently listed with another broker, this is not intended as a solicitation of that listing.</div>
  </div>
  <div class="address-rule"></div>
</section>

</body>
</html>
```